re brand of safeguardly.pro to Vexawatch.co.uk

We would like a new site design for our safeguardly.pro site

the new domain is Vexawatch.co.uk

we like the blue colour smiler to this site http://www.fundsentrypal.co.uk, and we would like real images o people using instead of cartons

you can take inspiration from the credit ref agency monthly membership site but this product is not a credit report we just like that look

https://www.loanharbor.co.uk
http://www.fundsentrypal.co.uk/
https://www.brimzo.co.uk/

Reason: we have added more details to the project brief and also increased the budget and committed to buying a design

We have guaranteed the project extend the dead line and increased the payment we have also added more details in the brief to give you guys more direction I am looking forward to seeing the designs

Target Market(s)

18 to 50 yo concerned with the privacy and id fraud

The bulk of clients our aged 18 to 30 so a fresh feel is important

Industry/Entity Type

Domain

Colors
33a6d7
0592cd
0555a3
3176b5
85cae6

```html
<!DOCTYPE html>
<html lang="en">
<head>
<meta charset="utf-8">
<title>Vexawatch.co.uk – Signup</title>
<link href="https://fonts.googleapis.com/css2?family=Open+Sans:wght@400;600;700&display=swap" rel="stylesheet">
<style>
:root{
  --blue:#0a9bd6;
  --blue-dark:#0788c0;
  --green:#5dc43b;
  --navy:#1a2535;
  --ink:#2f3a44;
  --grey-text:#6b7176;
  --band:#eef1f3;
  --halo:#e2e6e9;
  --white:#ffffff;
  --line:#e4e7ea;
}
*{margin:0;padding:0;box-sizing:border-box}
html,body{width:1155px;height:1200px;overflow:hidden;background:var(--white);font-family:"Open Sans",Arial,sans-serif;color:var(--ink)}
.page{position:relative;width:1155px;height:1200px}

/* header */
.site-header{position:absolute;top:0;left:0;width:100%;height:66px}
.brand{position:absolute;left:144px;top:16px;display:flex;align-items:center;gap:8px}
.brand-dot{width:32px;height:32px;border-radius:50%;background:var(--blue)}
.brand-name{font-size:20px;font-weight:400;color:#4a5259;letter-spacing:.2px}
.main-nav{position:absolute;right:144px;top:18px;display:flex;align-items:center;gap:18px;font-size:12px;color:#6d737a}
.main-nav .active{color:var(--blue)}
.btn-login{background:var(--green);color:var(--white);font-weight:700;font-size:11px;padding:9px 13px;border-bottom:2px solid #4aa62d}

/* hero */
.hero{position:absolute;top:66px;left:0;width:100%;height:137px;background:linear-gradient(100deg,#1c2738,#263246 55%,#1b2536)}
.hero-title{position:absolute;left:143px;top:46px;font-size:38px;font-weight:400;color:var(--white)}
.hero-title strong{font-weight:700}
.hero-points{position:absolute;left:767px;top:32px;list-style:none;color:var(--white);font-size:18px;line-height:25.5px}
.hero-points li{display:flex;align-items:center;gap:10px}
.badge{position:absolute;left:912px;top:22px;width:100px;height:100px}

/* signup */
.signup-heading{position:absolute;left:144px;top:244px;font-size:27px;font-weight:600;color:var(--ink)}
.steps{position:absolute;left:144px;top:294px;width:867px;height:53px}
.step{position:absolute;top:8px;text-align:center;color:var(--white);line-height:1}
.step b{display:block;font-size:18px;font-weight:600}
.step span{display:block;font-size:11px;font-weight:600;margin-top:4px}
.form-panel{position:absolute;left:144px;top:347px;width:867px;height:293px;background:var(--blue)}
.field{position:absolute;width:256px;height:43px;background:var(--white);font-size:11px;color:#50575e;padding:0 14px;display:flex;align-items:center}
.btn-next{position:absolute;width:256px;height:43px;background:var(--green);color:var(--white);font-weight:600;font-size:14px;display:flex;align-items:center;justify-content:center;gap:8px;border-bottom:2px solid #4aa62d}

/* features */
.features{position:absolute;top:701px;left:0;width:100%;height:178px;background:var(--band)}
.feature{position:absolute;width:160px;text-align:center}
.feature-halo{position:absolute;width:133px;height:133px;border-radius:50%;background:var(--halo)}
.feature-circle{position:absolute;width:121px;height:121px;border-radius:50%;background:var(--blue);display:flex;align-items:center;justify-content:center}
.feature-label{position:absolute;font-size:18px;font-weight:600;color:var(--ink);width:200px;text-align:center}
.operator{position:absolute;color:#d3d8dc}

/* subscribe */
.subscribe{position:absolute;top:879px;left:0;width:100%;height:190px;background:var(--green);text-align:center;color:var(--white)}
.subscribe h2{margin-top:27px;font-size:27px;font-weight:600;letter-spacing:.3px}
.subscribe p{font-size:15px;margin-top:2px}
.subscribe-form{position:absolute;left:396px;top:110px;display:flex}
.subscribe-input{width:265px;height:43px;background:var(--white);color:#8a9096;font-size:11px;display:flex;align-items:center;padding-left:15px}
.subscribe-btn{width:98px;height:43px;background:#c2c7cb;color:var(--white);font-size:11px;font-weight:600;display:flex;align-items:center;justify-content:center}

/* footer */
.social{position:absolute;top:1069px;left:0;width:100%;height:60px;border-bottom:1px solid var(--line);display:flex;justify-content:center;align-items:center;gap:24px}
.social i{width:14px;height:14px;border-radius:50%;background:#9aa0a5;display:block}
.footer-links{position:absolute;top:1148px;left:0;width:100%;display:flex;justify-content:center;gap:16px;font-size:11px;color:#6b7176}
.footer-links .active{color:var(--blue)}
.copyright{position:absolute;top:1168px;left:0;width:100%;text-align:center;font-size:11px;color:#6b7176}
.copyright span{color:var(--blue)}
</style>
</head>
<body>
<div class="page">

  <header class="site-header">
    <div class="brand"><span class="brand-dot"></span><span class="brand-name">VEXAWATCH.CO.UK</span></div>
    <nav class="main-nav">
      <span>HOME</span><span>SOCIAL</span><span>ID ALERT</span><span>BANK ALERT</span><span class="active">SIGNUP</span><span>CONTACT</span>
      <span class="btn-login">MEMBER LOGIN</span>
    </nav>
  </header>

  <section class="hero" role="img" aria-label="Dark navy banner with a faint geometric background">
    <h1 class="hero-title">Signup <strong>Protection!</strong></h1>
    <ul class="hero-points">
      <li><svg width="15" height="15" viewBox="0 0 16 16"><circle cx="8" cy="8" r="7" fill="none" stroke="#1ba6de" stroke-width="1.5"/><path d="M6.5 5l3 3-3 3" fill="none" stroke="#1ba6de" stroke-width="1.5"/></svg>SECURE</li>
      <li><svg width="15" height="15" viewBox="0 0 16 16"><circle cx="8" cy="8" r="7" fill="none" stroke="#1ba6de" stroke-width="1.5"/><path d="M6.5 5l3 3-3 3" fill="none" stroke="#1ba6de" stroke-width="1.5"/></svg>RELIABLE</li>
      <li><svg width="15" height="15" viewBox="0 0 16 16"><circle cx="8" cy="8" r="7" fill="none" stroke="#1ba6de" stroke-width="1.5"/><path d="M6.5 5l3 3-3 3" fill="none" stroke="#1ba6de" stroke-width="1.5"/></svg>HELPFULL</li>
    </ul>
    <svg class="badge" viewBox="0 0 100 100">
      <polygon fill="#1ba6de" points="50,0 56,11 67,3 69,16 82,12 80,25 93,26 86,37 98,43 88,52 97,62 84,66 89,79 76,79 76,92 64,87 59,99 50,90 41,99 36,87 24,92 24,79 11,79 16,66 3,62 12,52 2,43 14,37 7,26 20,25 18,12 31,16 33,3 44,11"/>
      <g transform="rotate(-25 50 50)" fill="#fff" font-family="Open Sans, sans-serif" text-anchor="middle">
        <text x="50" y="36" font-size="8" font-weight="600">FILL DETAIL IN</text>
        <text x="50" y="58" font-size="22" font-weight="700">05-10</text>
        <text x="50" y="69" font-size="8" font-weight="600">MIN ONLY</text>
      </g>
    </svg>
  </section>

  <h2 class="signup-heading">SIGNUP</h2>

  <div class="steps">
    <svg width="867" height="53" viewBox="0 0 867 53" style="position:absolute;left:0;top:0">
      <rect width="867" height="53" fill="#0789bf"/>
      <polygon points="0,0 547,0 576,26.5 547,53 0,53" fill="#0895cc"/>
      <polygon points="0,0 260,0 289,26.5 260,53 0,53" fill="#5dc43b"/>
      <polyline points="547,0 576,26.5 547,53" fill="none" stroke="#067aab" stroke-width="3"/>
    </svg>
    <div class="step" style="left:0;width:289px"><b>STEP 1</b><span>YOUR DETAILS</span></div>
    <div class="step" style="left:289px;width:288px"><b>STEP 2</b><span>BANK DETAILS</span></div>
    <div class="step" style="left:577px;width:290px"><b>STEP 3</b><span>SUMMARY</span></div>
  </div>

  <form class="form-panel">
    <div class="field" style="left:24px;top:27px">TITLE</div>
    <div class="field" style="left:305px;top:27px">FIRST NAME</div>
    <div class="field" style="left:586px;top:27px">LAST NAME</div>
    <div class="field" style="left:24px;top:93px">EMAIL</div>
    <div class="field" style="left:305px;top:93px">CONFIRM EMAIL</div>
    <div class="field" style="left:586px;top:93px">DATE OF BIRTH (DD/MM/YYYY)</div>
    <div class="field" style="left:24px;top:160px">MOBILE</div>
    <div class="field" style="left:305px;top:160px">POST CODE</div>
    <div class="field" style="left:586px;top:160px">HOUSE NAME/NUMBER (OR FLAT NAME, ETC)</div>
    <div class="field" style="left:24px;top:227px">STREET</div>
    <div class="field" style="left:305px;top:227px">CITY/TOWN</div>
    <div class="btn-next" style="left:586px;top:227px">NEXT STEP
      <svg width="19" height="19" viewBox="0 0 20 20"><circle cx="10" cy="10" r="8.5" fill="none" stroke="#fff" stroke-width="1.6"/><path d="M8.5 6l4 4-4 4" fill="none" stroke="#fff" stroke-width="1.6"/></svg>
    </div>
  </form>

  <section class="features">
    <div class="feature-halo" style="left:221px;top:-17px"></div>
    <div class="feature-halo" style="left:410px;top:-17px"></div>
    <div class="feature-halo" style="left:601px;top:-17px"></div>
    <div class="feature-halo" style="left:802px;top:-17px"></div>

    <div class="feature-circle" style="left:226px;top:-3px">
      <svg width="74" height="74" viewBox="0 0 74 74" fill="#fff" stroke="#fff" stroke-width="3">
        <line x1="37" y1="38" x2="12" y2="30"/><line x1="37" y1="38" x2="60" y2="28"/><line x1="37" y1="38" x2="26" y2="16"/><line x1="37" y1="38" x2="50" y2="16"/><line x1="37" y1="38" x2="18" y2="55"/><line x1="37" y1="38" x2="27" y2="66"/><line x1="37" y1="38" x2="58" y2="52"/>
        <circle cx="12" cy="30" r="5"/><circle cx="60" cy="28" r="5"/><circle cx="26" cy="16" r="4"/><circle cx="50" cy="16" r="4"/><circle cx="27" cy="66" r="5"/><circle cx="58" cy="52" r="4"/>
        <circle cx="37" cy="28" r="6"/><path d="M27 46 q10 -14 20 0 z"/>
      </svg>
    </div>
    <div class="feature-circle" style="left:416px;top:-3px">
      <svg width="70" height="70" viewBox="0 0 70 70" fill="none" stroke="#fff" stroke-width="4">
        <rect x="6" y="14" width="58" height="44" rx="4"/><rect x="27" y="8" width="16" height="10" fill="#fff"/>
        <circle cx="22" cy="32" r="5" fill="#fff" stroke="none"/><path d="M12 49 q10 -14 20 0 z" fill="#fff" stroke="none"/>
        <line x1="38" y1="32" x2="56" y2="32"/><line x1="38" y1="42" x2="56" y2="42"/>
      </svg>
    </div>
    <div class="feature-circle" style="left:607px;top:-3px">
      <svg width="72" height="72" viewBox="0 0 72 72" fill="#fff">
        <polygon points="36,6 66,22 6,22"/><rect x="8" y="25" width="56" height="5"/>
        <rect x="11" y="33" width="5" height="24"/><rect x="19" y="33" width="5" height="24"/><rect x="48" y="33" width="5" height="24"/><rect x="56" y="33" width="5" height="24"/>
        <text x="36" y="54" font-size="22" font-weight="700" text-anchor="middle" font-family="Open Sans, sans-serif">$</text>
        <rect x="6" y="60" width="60" height="6"/>
      </svg>
    </div>
    <div class="feature-circle" style="left:808px;top:-3px"></div>

    <svg class="operator" style="left:364px;top:42px" width="34" height="34" viewBox="0 0 34 34"><rect x="13" y="0" width="8" height="34" fill="currentColor"/><rect x="0" y="13" width="34" height="8" fill="currentColor"/></svg>
    <svg class="operator" style="left:554px;top:42px" width="34" height="34" viewBox="0 0 34 34"><rect x="13" y="0" width="8" height="34" fill="currentColor"/><rect x="0" y="13" width="34" height="8" fill="currentColor"/></svg>
    <svg class="operator" style="left:751px;top:44px" width="34" height="26" viewBox="0 0 34 26"><rect x="0" y="2" width="34" height="8" fill="currentColor"/><rect x="0" y="16" width="34" height="8" fill="currentColor"/></svg>

    <div class="feature-label" style="left:187px;top:132px">Social Alert</div>
    <div class="feature-label" style="left:376px;top:132px">ID Alert</div>
    <div class="feature-label" style="left:567px;top:132px">Bank Alert</div>
    <div class="feature-label" style="left:768px;top:132px">Vexawatch.Co.Uk</div>
  </section>

  <section class="subscribe">
    <h2>SUBSCRIBE TO OUR UPDATES</h2>
    <p>Subscribe to your email newsletter for best venues</p>
    <div class="subscribe-form">
      <div class="subscribe-input">ENTER YOUR EMAIL ID</div>
      <div class="subscribe-btn">SUBSCRIBE</div>
    </div>
  </section>

  <div class="social"><i></i><i></i><i></i><i></i><i></i><i></i></div>

  <nav class="footer-links">
    <span class="active">Home</span><span>Social</span><span>Id Alert</span><span>Bank Alert</span><span>Signup</span><span>Contact</span>
  </nav>
  <p class="copyright">Copyright © 2015 <span>Vexawatch</span>. All Rights Reserved</p>

</div>
</body>
</html>
```